Business Card design for Recruiter providing Recruitment Staff Augmentation services

I need a double sided business card. I have used Plix to print cards in the past and really like their quality. I have a logo but need to change the tagline that is part of the graphic.

The tagline currently reads and Connnecting people with careers - but it should be removed.

The back should look like a notecard for writing a to do list with the first to-do Augment Recruiting Staff

```html
<!DOCTYPE html>
<html lang="en">
<head>
<meta charset="utf-8">
<title>Talent Summit business card</title>
<link rel="stylesheet" href="https://fonts.googleapis.com/css2?family=Montserrat:wght@400;600;700&display=swap">
<style>
  :root {
    --backdrop: #ececec;
    --card: #ffffff;
    --navy: #1f3a5f;
    --rust: #c5492b;
    --ink: #3a3f47;
    --rule: #5a7399;
  }
  * { margin: 0; padding: 0; box-sizing: border-box; }
  html, body { width: 1200px; height: 808px; overflow: hidden; }
  body {
    background: var(--backdrop);
    font-family: "Montserrat", sans-serif;
    position: relative;
  }
  .card {
    position: absolute;
    top: 262px;
    width: 500px;
    height: 286px;
    background: var(--card);
    box-shadow: 0 2px 10px rgba(0,0,0,0.08);
    overflow: hidden;
  }
  .card--front { left: 70px; }
  .card--back { left: 630px; }

  .brand {
    position: absolute;
    left: 30px;
    top: 30px;
    display: flex;
    align-items: center;
    gap: 12px;
  }
  .brand__dot {
    width: 26px; height: 26px;
    border-radius: 50%;
    background: var(--navy);
  }
  .brand__name {
    color: var(--navy);
    font-weight: 600;
    font-size: 30px;
    letter-spacing: 3px;
    text-transform: uppercase;
  }
  .contact {
    position: absolute;
    left: 30px;
    top: 104px;
  }
  .contact__name {
    color: var(--navy);
    font-weight: 700;
    font-size: 17px;
    letter-spacing: 0.5px;
    text-transform: uppercase;
    margin-bottom: 10px;
  }
  .contact__list { list-style: none; }
  .contact__item {
    display: flex;
    align-items: center;
    gap: 10px;
    font-size: 12px;
    color: var(--ink);
    line-height: 19px;
  }
  .contact__icon { width: 11px; height: 11px; flex: none; }

  .front-band {
    position: absolute;
    left: 0; bottom: 0;
    width: 500px; height: 40px;
  }

  .back-mark {
    position: absolute;
    left: 40px; top: 22px;
    width: 120px; height: 120px;
    border-radius: 50%;
    border: 4px solid var(--rust);
  }
  .todo {
    position: absolute;
    left: 250px; top: 118px;
    width: 210px;
    list-style: none;
  }
  .todo__line {
    height: 19px;
    border-bottom: 1px solid var(--rule);
    font-size: 10px;
    color: var(--navy);
    line-height: 16px;
  }
</style>
</head>
<body>
  <section class="card card--front" aria-label="Card front">
    <div class="brand">
      <span class="brand__dot"></span>
      <span class="brand__name">Talent Summit</span>
    </div>
    <div class="contact">
      <p class="contact__name">Dana Whitlow, SPHR</p>
      <ul class="contact__list">
        <li class="contact__item">
          <svg class="contact__icon" viewBox="0 0 12 12"><path d="M2 1h3l1 3-2 1a7 7 0 0 0 3 3l1-2 3 1v3c-6 0-9-3-9-9z" fill="var(--rust)"/></svg>
          303 555 0142
        </li>
        <li class="contact__item">
          <svg class="contact__icon" viewBox="0 0 12 12"><rect x="0.5" y="2" width="11" height="8" fill="none" stroke="var(--rust)"/><path d="M0.5 2l5.5 4.5L11.5 2" fill="none" stroke="var(--rust)"/></svg>
          dana@talentsummit.com
        </li>
        <li class="contact__item">
          <svg class="contact__icon" viewBox="0 0 12 12"><circle cx="6" cy="6" r="5.2" fill="none" stroke="var(--rust)"/><path d="M0.8 6h10.4M6 0.8c-3 3-3 7.4 0 10.4M6 0.8c3 3 3 7.4 0 10.4" fill="none" stroke="var(--rust)" stroke-width="0.8"/></svg>
          www.talentsummit.com
        </li>
      </ul>
    </div>
    <svg class="front-band" viewBox="0 0 500 40" aria-hidden="true">
      <rect x="0" y="16" width="500" height="6" fill="var(--navy)"/>
      <polygon points="350,22 500,22 500,40 340,40" fill="var(--rust)"/>
    </svg>
  </section>

  <section class="card card--back" aria-label="Card back, to-do notecard">
    <div class="back-mark"></div>
    <ol class="todo">
      <li class="todo__line">Augment Recruiting Staff</li>
      <li class="todo__line"></li>
      <li class="todo__line"></li>
      <li class="todo__line"></li>
      <li class="todo__line"></li>
      <li class="todo__line"></li>
      <li class="todo__line"></li>
    </ol>
  </section>
</body>
</html>
```